Web Design Project for a new download application :-)

We need a website design and a logo design for a new website and desktop application.
The Website will be www.Fetchora.com
The installed application will be: Fetchora

Fetchora is a desktop application that searches and finds all kind of Media files (Movies, Games, Songs, software, etc..)
Fetchora will also manage the download process for the selected files.
Fetchora automates the whole search and download process.

User Flow:
users will initially visit the website.
user will download the application from the website
user will install the application on his computer.
user will run and use the application.

What makes our software special:
-Great search engine for searching media files.
-Very high speed downloads. maximum speeds.
-Allow used to Search by: file type, size, date, format
-Pause and resume downloads
-Get any file you want instantly.
-Unlimited Downloads.

We will need:
Logo
WebSite Design
Icons for the desktop application.

we need only PSDs - no codded pages are needed !

Design to the following screen Size & resolution: 1024 x 768

Target Market(s)

movies and music lovers.
users who download movies, games, softwares, music etc...

Industry/Entity Type

Software

Requirements
Must have
• must have download button

```html
<!DOCTYPE html>
<html lang="en">
<head>
<meta charset="utf-8">
<title>Fetchora – Download all kind of media files</title>
<link href="https://fonts.googleapis.com/css2?family=Ubuntu:wght@400;500;700&family=Open+Sans:wght@400;600&display=swap" rel="stylesheet">
<style>
  :root {
    --navy: #06182e;
    --navy-2: #0c2a4d;
    --hero-deep: #0a3d8f;
    --hero-light: #2b8fe6;
    --page: #f3f3f3;
    --text: #555555;
    --text-dark: #333333;
    --link-blue: #1b7cc8;
    --accent-orange: #f08a12;
    --accent-yellow: #fcd13a;
    --quote-grey: #b8b8b8;
    --footer-top: #2f8fe3;
    --footer-bottom: #1565c8;
    --white: #ffffff;
  }
  * { margin: 0; padding: 0; box-sizing: border-box; }
  html, body { width: 1200px; height: 1037px; overflow: hidden; }
  body { font-family: "Open Sans", Arial, sans-serif; background: var(--page); position: relative; }
  .abs { position: absolute; }

  .rainbow { left: 0; top: 0; width: 1200px; height: 6px;
    background: linear-gradient(90deg, #e8242d, #f7941d, #fff200, #39b54a, #00aeef, #2e3192, #92278f, #e8242d, #f7941d); }
  .site-header { left: 0; top: 6px; width: 1200px; height: 85px;
    background: linear-gradient(180deg, var(--navy-2), var(--navy)); }
  .brand { left: 110px; top: 14px; font-family: "Ubuntu", sans-serif; font-weight: 700;
    font-size: 50px; color: #d9dde2; letter-spacing: 1px; }
  .main-nav { left: 523px; top: 26px; display: flex; gap: 0; font-family: "Ubuntu", sans-serif;
    font-size: 17px; font-weight: 500; color: var(--white); }
  .main-nav a { color: var(--white); text-decoration: none; padding: 0 9px; line-height: 34px; }
  .main-nav a.current { background: linear-gradient(#ffffff, #dcdcdc); color: #111; border-radius: 3px;
    padding: 0 9px; margin-right: 9px; position: relative; }
  .main-nav a.current::after { content: ""; position: absolute; left: 26px; bottom: -7px;
    border: 7px solid transparent; border-bottom: 0; border-top-color: #dcdcdc; }
  .lang { left: 915px; top: 38px; font-size: 12px; color: var(--white); display: flex; align-items: center; gap: 6px; }
  .lang-box { width: 75px; height: 21px; background: var(--white); color: #333; font-size: 12px;
    padding: 2px 5px; position: relative; }
  .lang-box::after { content: ""; position: absolute; right: 5px; top: 8px;
    border: 4px solid transparent; border-top-color: #111; border-bottom: 0; }

  .hero { left: 0; top: 91px; width: 1200px; height: 324px; overflow: hidden;
    background: radial-gradient(ellipse at 50% 10%, var(--hero-light), var(--hero-deep) 70%, #0a2f70); }
  .devices { left: 113px; top: 120px; width: 562px; height: 320px; border-radius: 10px;
    background: linear-gradient(160deg, #2a2f36, #0e1216 60%, #c9ced3); }
  .hero-title { left: 652px; top: 124px; font-family: "Ubuntu", sans-serif; font-weight: 700;
    color: var(--white); font-size: 82px; line-height: 86px; letter-spacing: -1px; }
  .hero-sub { left: 655px; top: 205px; font-family: "Ubuntu", sans-serif; font-weight: 700;
    color: var(--white); font-size: 34px; line-height: 40px; }
  .hero-list { left: 656px; top: 243px; font-family: "Ubuntu", sans-serif; color: var(--accent-yellow);
    font-size: 25px; line-height: 32px; }
  .download-btn { left: 657px; top: 283px; width: 326px; height: 74px; border-radius: 4px;
    background: linear-gradient(#fde36b, #f7b81e); border: 1px solid #e9a413;
    font-family: "Ubuntu", sans-serif; font-weight: 700; font-size: 31px; color: #111;
    display: flex; align-items: center; justify-content: center; text-decoration: none; }

  .features-ribbon { left: 109px; top: 458px; width: 240px; height: 56px; }
  .features-title { left: 131px; top: 459px; font-family: "Ubuntu", sans-serif; font-size: 35px; color: var(--white); }

  .feature { top: 520px; width: 210px; text-align: center; }
  .feature h3 { font-family: "Ubuntu", sans-serif; font-weight: 400; font-size: 18px; line-height: 22px;
    color: var(--link-blue); margin-top: 76px; }
  .feature p { font-size: 12.5px; line-height: 18px; color: var(--text); margin-top: 7px; }
  .feature-icon { position: absolute; top: 4px; left: 50%; transform: translateX(-50%); }
  .col-rule { top: 530px; width: 1px; height: 200px; background: linear-gradient(transparent, #dcdcdc, transparent); }

  .quote-rule { left: 205px; top: 764px; width: 820px; height: 1px; background: #dcdcdc; }
  .quote-mark { font-family: Georgia, serif; font-size: 90px; color: var(--quote-grey); font-weight: 700; line-height: 1; }
  .testimonial { left: 174px; top: 797px; width: 862px; font-size: 12.5px; line-height: 18px; color: var(--text-dark); }
  .cite { left: 176px; top: 876px; font-size: 12px; color: var(--text-dark); }
  .cite .name { color: var(--accent-orange); }

  .site-footer { left: 0; top: 937px; width: 1200px; height: 100px;
    background: linear-gradient(var(--footer-top), var(--footer-bottom)); color: var(--white); }
  .footer-nav { left: 121px; top: 28px; font-size: 12.5px; display: flex; gap: 13px; }
  .footer-nav a, .contact a { color: var(--white); }
  .contact { left: 121px; top: 54px; font-size: 14px; font-weight: 600; }
  .contact small { font-size: 12.5px; font-weight: 400; }
  .footer-brand { left: 887px; top: 22px; font-family: "Ubuntu", sans-serif; font-weight: 700;
    font-size: 46px; color: #e4e8ec; }
</style>
</head>
<body>
  <div class="abs rainbow"></div>

  <header class="abs site-header">
    <div class="abs brand">Fetchora</div>
    <nav class="abs main-nav">
      <a class="current" href="#">HOME</a>
      <a href="#">DOWNLOAD</a>
      <a href="#">SUPPORT</a>
      <a href="#">AFFILIATES</a>
    </nav>
    <div class="abs lang">Select Language <span class="lang-box">English</span></div>
  </header>

  <section class="abs hero">
    <svg class="abs" width="1200" height="324" viewBox="0 0 1200 324" style="left:0;top:0">
      <path d="M0 250 C300 200 600 330 1200 200 L1200 324 L0 324Z" fill="#ffffff" opacity="0.08"/>
      <path d="M0 290 C400 240 700 330 1200 260" stroke="#9fd0ff" stroke-width="2" fill="none" opacity="0.4"/>
    </svg>
  </section>
  <div class="abs devices" role="img" aria-label="Desktop monitor and laptop showing the Fetchora file browser"></div>
  <div class="abs hero-title">DOWNLOAD</div>
  <div class="abs hero-sub">ALL KIND OF MEDIA FILES</div>
  <div class="abs hero-list">Movies, Games, Songs, Software, etc.</div>
  <a class="abs download-btn" href="#">DOWNLOAD Fetchora</a>

  <svg class="abs features-ribbon" viewBox="0 0 240 56">
    <polygon points="0,56 10,50 10,56" fill="#b35a00"/>
    <polygon points="0,0 225,0 240,24 225,48 0,48" fill="#f8a51b"/>
    <polygon points="0,0 225,0 240,24 0,24" fill="#f49312"/>
  </svg>
  <div class="abs features-title">Features</div>

  <svg class="abs" width="20" height="30" style="left:115px;top:620px"><path d="M16 2 L4 15 L16 28" stroke="#111" stroke-width="5" fill="none"/></svg>
  <svg class="abs" width="20" height="30" style="left:1064px;top:620px"><path d="M4 2 L16 15 L4 28" stroke="#111" stroke-width="5" fill="none"/></svg>

  <div class="abs feature" style="left:145px">
    <div class="feature-icon" role="img" aria-label="Magnifying glass over a film strip" style="width:66px;height:64px;border-radius:10px;background:linear-gradient(135deg,#9fd2f5,#4a4a4a)"></div>
    <h3>Great Search Engine for Searching Media Files</h3>
    <p>Lorem ipsum dolor sit amet, consectetur adipiscing elit. Sed mollis, ante placerat placerat varius, elit ante varius quam, sit amet dignissim purus urna vel</p>
  </div>
  <div class="abs col-rule" style="left:368px"></div>
  <div class="abs feature" style="left:380px">
    <svg class="feature-icon" width="64" height="64" viewBox="0 0 64 64">
      <circle cx="32" cy="32" r="30" fill="#e7e7e7"/><circle cx="32" cy="32" r="26" fill="#f07a10"/>
      <path d="M27 16 H37 V32 H45 L32 47 L19 32 H27Z" fill="#fff"/>
    </svg>
    <h3>Very High Speed Downloads</h3>
    <p>Curabitur convallis lectus quis tellus suscipit sollicitudin. Phasellus suscipit justo sit amet nisl rhoncus congue. Integer non egestas nibh.</p>
  </div>
  <div class="abs col-rule" style="left:601px"></div>
  <div class="abs feature" style="left:613px">
    <div class="feature-icon" role="img" aria-label="Document with green download arrow" style="width:62px;height:52px;border-radius:4px;background:linear-gradient(135deg,#f2f2f2,#9ccc4a)"></div>
    <h3>Search by: file type, size, date, format</h3>
    <p>Nulla vitae imperdiet elit. Quisque vehicula, nulla sit amet ultrices molestie, purus tortor consequat magna, et eleifend elit quam</p>
  </div>
  <div class="abs col-rule" style="left:834px"></div>
  <div class="abs feature" style="left:845px">
    <svg class="feature-icon" width="52" height="52" viewBox="0 0 52 52">
      <circle cx="26" cy="26" r="24" fill="#1b3fa8"/>
      <rect x="18" y="15" width="6" height="22" rx="1" fill="#fff"/><rect x="28" y="15" width="6" height="22" rx="1" fill="#fff"/>
    </svg>
    <h3>Pause and Resume Downloads</h3>
    <p>Mauris eu quam sit amet sem suscipit rhoncus. Ut mauris dolor, bibendum at lacinia sit amet, dictum a justo. Aliquam ac est nunc, in suscipit libero.</p>
  </div>

  <div class="abs quote-rule"></div>
  <div class="abs quote-mark" style="left:114px;top:770px">“</div>
  <blockquote class="abs testimonial">Aenean nunc dui, varius vitae auctor eu, tincidunt adipiscing sem. Praesent massa nibh, imperdiet eget luctus vel, suscipit sit amet augue. Donec risus lacus, luctus nec condimentum non, venenatis eu risus. Vestibulum lorem nunc, placerat nec blandit at, mollis a justo. In faucibus lacus a magna congue id auctor lectus tristique. Aenean imperdiet bibendum est, ut accumsan neque bibendum quis. Quisque non enim eget lacus hendrerit faucibus. Nullam est erat, posuere vitae sodales</blockquote>
  <div class="abs cite"><span class="name">Dana Keller</span> &nbsp;|&nbsp; Perth</div>
  <div class="abs quote-mark" style="left:1048px;top:852px">”</div>

  <footer class="abs site-footer">
    <nav class="abs footer-nav">
      <a href="#">HOME</a><a href="#">DOWNLOAD</a><a href="#">SUPPORT</a><a href="#">AFFILIATES</a>
    </nav>
    <div class="abs contact">email : <a href="#">contact@fetchora.com</a> &nbsp;|&nbsp; Call us - 0198765432 &nbsp;|&nbsp; <small>©2011 Fetchora. All rights reserved</small></div>
    <div class="abs footer-brand">Fetchora</div>
  </footer>
</body>
</html>
```